T.B.W.L. Business Card Design

we need a business card design for a motor vehicle repair business in Southport Australia, called Trevan's Automotive Repair Services. Our services include panel & paint, resprays and light bodyworks. We have a logo which we would like to use on the business card. We would like to see designs that use the colours blue and grey.

Industry/Entity Type

Automotive

Contact Information for Business Card

Trevan's Automotive Repair Services,
Delwyn Orsk,
7/2-4 Quarrow Street Marlowe Bay 4298, 0471 862 307, /trevansautomotiverepairservices, trevansautomotiverepairservices@examplemail.test,
services: panel & paint, respray, light bodyworks.
ABN: 47 612 098 254

Requirements
Must have
• Front of card must include attached logo and contact details.
please list services
Your eye should be drawn to the name (Delwyn Orsk) and phone number (0471 862 307).
Font must be legible and contemporary.
back of business card should have the following:
1. title - quote and
2. list the following: for, date, valid till, quote details and
3. a footer "to book you repair, please contact Delwyn Orsk on 0471 862 307".
There needs to be enough space to hand write details.
Should not have
• do not include any graphics/illustrations.

```html
<!DOCTYPE html>
<html lang="en">
<head>
<meta charset="utf-8">
<title>Trevan's Automotive Repair Services – Business Card</title>
<link rel="stylesheet" href="https://fonts.googleapis.com/css2?family=Open+Sans:ital,wght@0,400;0,600;0,700;1,600&display=swap">
<style>
  :root {
    --stage: #d9d9d9;
    --card-white: #ffffff;
    --card-blue: #b9d3f0;
    --brand-blue: #1f6fb5;
    --ink: #2b2b2b;
    --grey-dark: #6e6e6e;
    --grey-mid: #8c8c8c;
    --rule: #9a9a9a;
  }
  * { box-sizing: border-box; margin: 0; padding: 0; }
  html, body { width: 1200px; height: 646px; overflow: hidden; }
  body {
    background: var(--stage);
    font-family: "Open Sans", Arial, sans-serif;
    color: var(--ink);
    position: relative;
  }
  .card {
    position: absolute;
    top: 173px;
    width: 525px;
    height: 300px;
    border-radius: 6px;
    overflow: hidden;
    box-shadow: 0 6px 18px rgba(0,0,0,.18);
  }

  /* ---------- Back: quote side ---------- */
  .card--back { left: 45px; background: var(--card-white); }
  .quote-title {
    height: 40px;
    background: linear-gradient(#8a8a8a, var(--grey-dark));
    color: #fff;
    font-size: 18px;
    font-weight: 600;
    letter-spacing: 2px;
    text-align: center;
    line-height: 40px;
  }
  .quote-lines { margin: 6px 22px 0; }
  .quote-line { height: 24px; border-bottom: 1px solid var(--rule); }
  .quote-total {
    margin: 8px 22px 0;
    height: 22px;
    background: var(--grey-mid);
    color: #fff;
    font-size: 15px;
    font-weight: 700;
    display: flex;
    justify-content: flex-end;
    align-items: center;
    gap: 38px;
    padding-right: 16px;
  }
  .quote-fields {
    position: absolute;
    left: 22px;
    bottom: 18px;
    width: 180px;
  }
  .quote-field {
    display: flex;
    align-items: flex-end;
    height: 30px;
    border-bottom: 1px solid var(--rule);
    font-size: 15px;
    font-weight: 600;
    color: var(--ink);
    gap: 30px;
    padding-left: 76px;
    position: relative;
  }
  .quote-field__label {
    position: absolute;
    left: 0;
    bottom: 0;
    background: var(--grey-mid);
    color: #fff;
    font-size: 12px;
    font-weight: 600;
    padding: 2px 8px;
  }
  .quote-footer {
    position: absolute;
    right: 22px;
    bottom: 16px;
    width: 290px;
    white-space: nowrap;
  }
  .quote-footer__lead { font-size: 13px; color: var(--ink); }
  .quote-footer__contact { font-size: 19px; font-weight: 700; line-height: 1.2; }
  .services {
    font-size: 11.5px;
    font-weight: 600;
    margin-top: 3px;
    letter-spacing: .2px;
    white-space: nowrap;
  }
  .services__sep { color: var(--brand-blue); font-weight: 700; margin: 0 5px; }

  /* ---------- Front: contact side ---------- */
  .card--front { left: 630px; background: var(--card-blue); }
  .front-panel {
    position: absolute;
    left: 12px; right: 12px; top: 12px;
    height: 196px;
    background: var(--card-white);
    border-radius: 10px;
    box-shadow: 0 2px 5px rgba(0,0,0,.18);
    padding: 12px 18px 0;
  }
  .front-panel .services { text-align: right; font-size: 11px; }
  .brand {
    display: flex;
    align-items: center;
    gap: 10px;
    margin-top: 22px;
  }
  .brand__dot {
    width: 34px; height: 34px;
    border-radius: 50%;
    background: var(--brand-blue);
    flex: none;
  }
  .brand__name {
    font-size: 21px;
    font-weight: 700;
    color: var(--brand-blue);
    line-height: 1.15;
  }
  .person {
    position: absolute;
    left: 18px; right: 18px; bottom: 14px;
    display: flex;
    justify-content: space-between;
    align-items: baseline;
  }
  .person__name { font-size: 21px; font-style: italic; font-weight: 600; color: var(--grey-dark); }
  .person__phone { font-size: 20px; font-weight: 600; color: var(--grey-dark); }
  .contact-list {
    position: absolute;
    left: 24px; bottom: 12px;
    list-style: none;
  }
  .contact-list li {
    display: flex;
    align-items: center;
    gap: 9px;
    font-size: 13px;
    font-weight: 600;
    color: var(--ink);
    height: 25px;
    white-space: nowrap;
  }
  .contact-icon { width: 17px; height: 17px; flex: none; }
</style>
</head>
<body>

  <section class="card card--back" aria-label="Quote side of business card">
    <h2 class="quote-title">QUOTE</h2>
    <div class="quote-lines">
      <div class="quote-line"></div>
      <div class="quote-line"></div>
      <div class="quote-line"></div>
    </div>
    <div class="quote-total"><span>$</span><span>.</span></div>

    <div class="quote-fields">
      <div class="quote-field"><span class="quote-field__label">valid till</span><span>/</span><span>/</span></div>
      <div class="quote-field"><span class="quote-field__label">date</span><span>/</span><span>/</span></div>
    </div>

    <div class="quote-footer">
      <p class="quote-footer__lead">To book your repair please contact</p>
      <p class="quote-footer__contact">Delwyn Orsk on 0471 862 307</p>
      <p class="services">PANEL &amp; PAINT<span class="services__sep">|</span>RESPRAY<span class="services__sep">|</span>LIGHT BODYWORKS</p>
    </div>
  </section>

  <section class="card card--front" aria-label="Contact side of business card">
    <div class="front-panel">
      <p class="services">PANEL &amp; PAINT<span class="services__sep">|</span>RESPRAY<span class="services__sep">|</span>LIGHT BODYWORKS</p>
      <div class="brand">
        <span class="brand__dot"></span>
        <span class="brand__name">Trevan's Automotive<br>Repair Services</span>
      </div>
      <div class="person">
        <span class="person__name">Delwyn Orsk</span>
        <span class="person__phone">Phone: 0471 862 307</span>
      </div>
    </div>

    <ul class="contact-list">
      <li>
        <svg class="contact-icon" viewBox="0 0 20 20" aria-hidden="true">
          <circle cx="10" cy="10" r="10" fill="var(--brand-blue)"/>
          <path d="M10 4a4 4 0 0 0-4 4c0 3 4 8 4 8s4-5 4-8a4 4 0 0 0-4-4z" fill="#fff"/>
          <circle cx="10" cy="8" r="1.5" fill="var(--brand-blue)"/>
        </svg>
        Unit 7/2-4 Quarrow Street Marlowe Bay 4298
      </li>
      <li>
        <svg class="contact-icon" viewBox="0 0 20 20" aria-hidden="true">
          <circle cx="10" cy="10" r="10" fill="var(--brand-blue)"/>
          <rect x="5" y="6.5" width="10" height="7" fill="#fff"/>
          <path d="M5 6.5l5 4 5-4" fill="none" stroke="var(--brand-blue)" stroke-width="1.2"/>
        </svg>
        trevansautomotiverepairservices@examplemail.test
      </li>
      <li>
        <svg class="contact-icon" viewBox="0 0 20 20" aria-hidden="true">
          <circle cx="10" cy="10" r="10" fill="var(--brand-blue)"/>
        </svg>
        ABN: 47 612 098 254
      </li>
    </ul>
  </section>

</body>
</html>
```